Poster design for - Glowing Meadow Festival

To design a dynamic illustrated Glowing Meadow Festival poster.
The dates are: 3-5 July 2020
Location: Tarlow Campsite, Ashbrook, Marlshire
www.glowingmeadow.co.uk

Here is some text about the event to give you an idea. You can take elements from it if you like:

A Gathering of Female Energy to Ignite and Embrace the Power of Woman with Mother Earth.

Target Market(s)

Women festival goers.

Industry/Entity Type

Festival

Colors

Designer to choose colors to be used in the design.

Requirements
Must have
• Glowing Meadow Logo - but this can be altered to look washed out.
• Date, location, website url.
Nice to have
• Earthy, hippy, festival look.

```html
<!DOCTYPE html>
<html lang="en">
<head>
<meta charset="utf-8">
<title>Glowing Meadow Festival Poster</title>
<link rel="stylesheet" href="https://fonts.googleapis.com/css2?family=Marcellus&family=Montserrat:wght@500&family=Rajdhani:ital,wght@0,500;0,700;1,700&family=Roboto:wght@400;700&display=swap">
<style>
  :root {
    --page: #ececec;
    --night: #100a0c;
    --ember: #e8573a;
    --ember-deep: #c9302a;
    --white: #ffffff;
    --muted: #e6e0de;
  }
  * { margin: 0; padding: 0; box-sizing: border-box; }
  html, body { width: 1200px; height: 830px; overflow: hidden; background: var(--page); }
  .poster {
    position: absolute; left: 320px; top: 19px; width: 560px; height: 792px; overflow: hidden;
    background:
      radial-gradient(ellipse 60% 18% at 70% 6%, rgba(150,40,40,.55), transparent 70%),
      radial-gradient(ellipse 50% 22% at 20% 4%, rgba(110,30,40,.45), transparent 70%),
      radial-gradient(ellipse 70% 30% at 50% 35%, rgba(60,20,30,.5), transparent 70%),
      var(--night);
    color: var(--white);
    text-align: center;
  }
  .poster > * { position: absolute; }
  .figure-art {
    left: 327px; top: 350px; width: 260px; height: 470px;
    border-radius: 60% 20% 0 40% / 30% 10% 0 50%;
    background: radial-gradient(ellipse at 45% 35%, #a5382c, #7a1e1e 55%, #3a0e10 100%);
    opacity: .9;
  }
  .welcome { top: 32px; left: 0; width: 100%; font: 500 17px/1 'Montserrat', sans-serif; letter-spacing: 7px; }
  .title-top { top: 66px; left: 0; width: 100%; font: 400 72px/1 'Marcellus', serif; color: var(--ember); letter-spacing: 1px; }
  .title-main { top: 132px; left: 0; width: 100%; font: 400 86px/1 'Marcellus', serif; letter-spacing: -1px; }
  .title-sub { top: 226px; left: 0; width: 100%; font: 400 44px/1 'Marcellus', serif; color: var(--ember); letter-spacing: 20px; padding-left: 20px; }
  .tagline { top: 288px; left: 40px; width: 480px; font: 400 13.5px/1.45 'Roboto', sans-serif; color: var(--muted); }
  .motto { top: 334px; left: 0; width: 100%; font: 400 25px/1 'Marcellus', serif; color: var(--ember); letter-spacing: 1px; }
  .weekend-band {
    top: 384px; left: 0; width: 309px; height: 28px; background: var(--ember-deep);
    border-radius: 0 14px 14px 0;
    font: italic 700 22px/28px 'Rajdhani', sans-serif; text-align: left; padding-left: 34px;
  }
  .date-month { top: 420px; left: 10px; width: 300px; font: 500 42px/1 'Rajdhani', sans-serif; color: var(--ember); letter-spacing: 1px; }
  .date-days { top: 456px; left: 10px; width: 300px; font: 700 72px/1 'Rajdhani', sans-serif; letter-spacing: 1px; }
  .glow-line { top: 524px; left: 30px; width: 250px; height: 2px; background: radial-gradient(ellipse at center, #ffb08a, var(--ember) 20%, transparent 70%); }
  .details { top: 536px; left: 32px; text-align: left; }
  .details p { font: 400 13px/1.5 'Roboto', sans-serif; color: var(--muted); }
  .details .venue { margin-top: 4px; font: 700 21px/1.2 'Roboto', sans-serif; color: var(--ember); }
  .brand { top: 700px; left: 32px; display: flex; align-items: center; gap: 10px; font: 400 24px/1 'Marcellus', serif; color: var(--ember); }
  .brand-dot { width: 14px; height: 14px; border-radius: 50%; background: var(--ember); }
  .website { top: 756px; left: 32px; font: 400 16px/1 'Roboto', sans-serif; }
</style>
</head>
<body>
  <main class="poster">
    <div class="figure-art" role="img" aria-label="Fiery red silhouette of a woman's profile with head tilted back"></div>
    <p class="welcome">WELCOME TO</p>
    <h1 class="title-top">GLOWING</h1>
    <p class="title-main">MEADOW</p>
    <p class="title-sub">FESTIVAL</p>
    <p class="tagline">A Gathering of Female Energy to Ignite and Embrace the Power of<br>Woman with Mother Earth.</p>
    <p class="motto">IN THE HEART OF THE FIRE!</p>
    <p class="weekend-band">JOIN US FOR THE WEEKEND</p>
    <p class="date-month">JULY 2020</p>
    <p class="date-days">3RD-5TH</p>
    <div class="glow-line"></div>
    <div class="details">
      <p>For the 1st Glowing Meadow Festival<br>in the beautiful setting of</p>
      <p class="venue">Tarlow Campsite, Ashbrook in<br>Marlshire</p>
    </div>
    <div class="brand"><span class="brand-dot"></span>GLOWING MEADOW</div>
    <p class="website">www.glowingmeadow.co.uk</p>
  </main>
</body>
</html>
```